Webdesign für Reisebüro
Zielgruppe
Reisebüro - wir haben uns vor 20 Jahren auf Reisen nach Asien spezialisiert aber inzwischen ist unsere Kernkompetenz das individuelle Arrangieren von Fernreisen in alle Welt. Jedoch decken wir auch das komplette touristische Portfolio ab was natürlich auch nicht zu kurz kommen darf. Unsere Zielgruppe liegt tatsächlich zwischen 20—70
Aufgabenstellung
Wir bezeichnen uns als das besondere Reisebüro weil wir als Menschen besonders sind. Wir lieben es zu begeistern und das gelingt uns so gut dass wir seit bestimmt 15 Jahren komplett ohne Werbung auskommen und nur von Mundpropaganda leben. Das Design soll genau dieses Besondere zum Ausdruck bringen. Soll keine „klassische“ Reisebüroseite sein auf der man selbst Reisen suchen Und buchen kann.
Natürlich wird es zb eine Seite „Über uns“ und Zielgebietsinfos und noch andere Seiten geben. Primär geht es jetzt mal um das Design an sich das unser Programmierer dann sicher umsetzen kann.
Das Büro ist bisschen im Factory Style eingerichtet und wird aktuell noch mehr diesem Style angepasst.
Der Name Wander Nest spiegelt den chilligen Lifestyle wieder den wir verkörpern.

```html
<!DOCTYPE html>
<html lang="de">
<head>
<meta charset="utf-8">
<title>Wander Nest – Das besondere Reisebüro</title>
<link href="https://fonts.googleapis.com/css2?family=Marcellus&family=Raleway:ital,wght@0,300;0,400;1,300;1,400&display=swap" rel="stylesheet">
<style>
:root{
  --page:#ffffff;
  --panel:#ebebeb;
  --maroon:#8a5566;
  --green:#7c9a5c;
  --text:#5a5a5a;
  --footer:#474c4f;
  --footer-text:#e4e4e4;
  --white:#ffffff;
  --ring:#55585b;
}
*{margin:0;padding:0;box-sizing:border-box}
html,body{width:720px;height:1200px;overflow:hidden;background:var(--page)}
body{position:relative;font-family:'Raleway',sans-serif;color:var(--text)}
.abs{position:absolute}
.site{position:absolute;left:117px;top:23px;width:487px;height:1124px;background:var(--panel)}
.hero{position:absolute;left:117px;top:23px;width:487px;height:290px;
  background:linear-gradient(180deg,#7f9dc8 0%,#b7a9c4 14%,#d5b6b8 22%,#9db0b8 34%,#6f8f5a 50%,#86a869 62%,#c9d0c0 80%,#ebebeb 100%)}
.sideboard{position:absolute;left:262px;top:194px;width:134px;height:100px;
  background:linear-gradient(180deg,#7a5a48 0%,#8c6e5a 55%,rgba(235,235,235,0) 100%)}
.tagline{left:123px;top:25px;font-size:6.2px;font-style:italic;font-weight:300;color:var(--white);letter-spacing:.1px}
.nav-line{left:117px;width:487px;height:1px;background:rgba(255,255,255,.85)}
.nav a{position:absolute;top:66px;font-size:6.8px;color:var(--white);text-decoration:none;letter-spacing:.1px}
.hours-top{font-size:6.4px;font-style:italic;color:var(--white)}
.brand-seal{left:342px;top:49px;width:40px;height:40px;border-radius:50%;background:#f3f1ec;border:1.5px solid #6a6a6a;
  display:flex;align-items:center;justify-content:center;font-family:'Raleway',sans-serif;font-size:6px;font-weight:400;color:#4a4a4a;text-align:center;line-height:1.1}
.section-title{font-family:'Marcellus',serif;color:var(--maroon);font-size:13.5px;letter-spacing:.3px;white-space:nowrap}
.rule{height:1px;background:var(--maroon)}
.lead{left:117px;width:487px;top:340px;text-align:center;font-style:italic;font-weight:300;font-size:9.2px;color:#555}
.col-title{font-family:'Marcellus',serif;font-size:9px;letter-spacing:.2px}
.col-text{font-size:6.3px;line-height:8.1px;font-weight:300;color:var(--text)}
.photo{position:absolute}
.dest-band{left:118px;top:596px;width:486px;height:189px;
  background:linear-gradient(180deg,#8fb0cf 0%,#c7b2ab 18%,#b8a9a0 36%,#9cab8a 58%,#809d64 80%,#7f9c62 100%)}
.dest-title{left:118px;width:486px;top:599px;text-align:center;font-family:'Marcellus',serif;font-size:18px;color:rgba(255,255,255,.9)}
.dest{position:absolute;width:104px;height:104px;border-radius:50%;border:2px solid var(--ring);box-shadow:0 0 0 2px #f2f2f2 inset}
.dest-label{position:absolute;top:757px;width:104px;text-align:center;font-size:6.3px;color:var(--white)}
.about p{position:absolute;left:168px;width:405px;font-size:6.3px;line-height:8.1px;font-weight:300;color:var(--text)}
.footer{left:118px;top:1005px;width:485px;height:142px;background:var(--footer)}
.foot-brand{left:194px;top:1021px;font-size:10px;color:var(--white);font-family:'Raleway',sans-serif}
.foot-text{font-size:8.6px;line-height:10.7px;font-weight:300;color:var(--footer-text);white-space:nowrap}
.foot-head{left:435px;top:1023px;font-size:8px;letter-spacing:1.3px;color:var(--green)}
.foot-rule{left:190px;top:1101px;width:339px;height:1px;background:var(--green)}
.legal{left:195px;top:1111px;font-size:4.4px;color:#7c8083;letter-spacing:.2px;white-space:nowrap}
</style>
</head>
<body>
<div class="site"></div>

<header>
  <div class="hero" role="img" aria-label="Panorama der Chinesischen Mauer in grünen Bergen unter einem Abendhimmel"></div>
  <div class="sideboard" role="img" aria-label="Bunte Vintage-Kommode im Factory-Stil"></div>
  <div class="abs tagline">DAS BESONDERE REISEBÜRO</div>
  <div class="abs hours-top" style="left:506px;top:50px">MI Vormittag geschlossen</div>
  <div class="abs nav-line" style="top:62px"></div>
  <div class="abs nav-line" style="top:77px"></div>
  <nav class="nav">
    <a style="left:131px">HOME</a>
    <a style="left:173px">ÜBER UNS</a>
    <a style="left:221px">KONTAKT</a>
    <a style="left:265px">REISETIPPS</a>
    <a style="left:391px">IMPRESSUM</a>
    <a style="left:442px">DATENSCHUTZ</a>
  </nav>
  <div class="abs hours-top" style="left:504px;top:67px">MO-SA&nbsp; 10-13h&nbsp; MO-FR&nbsp; 14-18 h</div>
  <div class="abs brand-seal">Wander<br>Nest</div>
</header>

<section class="intro">
  <div class="abs rule" style="left:196px;top:328px;width:55px"></div>
  <div class="abs section-title" style="left:264px;top:319px">IHRE INDIVIDUELLE REISE</div>
  <div class="abs rule" style="left:458px;top:328px;width:64px"></div>
  <p class="abs lead">Kommen Sie zu uns auf eine gemütliche Tasse Kaffee und lassen Sich beraten</p>

  <div class="abs col-title" style="left:169px;top:436px;color:#6a6a6a">HEUTE HIER</div>
  <svg class="abs" style="left:232px;top:439px" width="13" height="7" viewBox="0 0 13 7"><path d="M0 0 L13 3.5 L0 7 L3 3.5 Z" fill="#555"/></svg>
  <p class="abs col-text" style="left:172px;top:456px;width:66px">Unser Wander-Nest in Augsburg ist seit&nbsp;&nbsp; 18 Jahren spezialisiert auf Reisen nach Asien, aber auch für den Rest der Welt.</p>
  <div class="photo" style="left:257px;top:419px;width:91px;height:123px;background:linear-gradient(160deg,#2a1a10 0%,#8a5a1e 45%,#d49a3a 75%,#5a3a14 100%)" role="img" aria-label="Abendliche Altstadt mit Brunnen und Figur"></div>

  <div class="abs col-title" style="left:376px;top:436px;color:var(--green)">MORGEN DORT</div>
  <svg class="abs" style="left:453px;top:431px" width="8" height="12" viewBox="0 0 8 12"><path d="M0.5 7 L3 11 L7.5 0.5" fill="none" stroke="var(--green)" stroke-width="1.6"/></svg>
  <p class="abs col-text" style="left:379px;top:455px;width:75px">Wir organisieren ihre individuelle Reise nach<br>Asien<br>USA<br>Kanada<br>Europa<br>und den Rest der Welt</p>
  <div class="photo" style="left:472px;top:418px;width:82px;height:123px;background:linear-gradient(180deg,#6f9ac4 0%,#4a7a4c 30%,#5aa3a6 60%,#8a6a4a 82%,#d9d4c8 100%)" role="img" aria-label="Longtail-Boote an einem tropischen Strand mit Felsen"></div>
</section>

<section>
  <div class="abs dest-band" role="img" aria-label="Weicher Himmel über grüner Landschaft"></div>
  <h2 class="abs dest-title" style="font-weight:400">Traumziele</h2>
  <div class="dest" style="left:133px;top:634px;background:radial-gradient(circle at 50% 40%,#f1f1f1 0%,#b9c6d6 45%,#6f8db4 100%)" role="img" aria-label="Weißer Tempel in Thailand"></div>
  <div class="dest" style="left:253px;top:634px;background:linear-gradient(180deg,#8fb6dc 0%,#c8d9e6 45%,#b0774a 70%,#4a3a34 100%)" role="img" aria-label="Brooklyn Bridge in New York"></div>
  <div class="dest" style="left:371px;top:634px;background:linear-gradient(180deg,#a7c4e0 0%,#e8ecef 30%,#5a6a5e 55%,#6b8a4a 75%,#a2a44e 100%)" role="img" aria-label="Bergsee in Kanada"></div>
  <div class="dest" style="left:488px;top:634px;background:linear-gradient(180deg,#4f8bd0 0%,#2f5a2a 40%,#4d7a3a 58%,#d9c49a 80%,#e7d7b4 100%)" role="img" aria-label="Palmenstrand in Sri Lanka"></div>
  <div class="dest-label" style="left:133px">THAILAND</div>
  <div class="dest-label" style="left:257px">USA</div>
  <div class="dest-label" style="left:375px">KANADA</div>
  <div class="dest-label" style="left:492px">SRI LANKA</div>
</section>

<section class="about">
  <div class="abs rule" style="left:196px;top:856px;width:55px"></div>
  <div class="abs section-title" style="left:329px;top:847px">ÜBER UNS</div>
  <div class="abs rule" style="left:458px;top:856px;width:64px"></div>
  <p style="top:879px">Das Wander Nest in Augsburg ist ein inhabergeführtes Reisebüro im Herzen von Augsburg. Bei uns werden Sie individuell und sehr ausführlich beraten, damit Ihre Reiseplanungen garantiert zum Erfolg werden. Wir freuen uns wenn Sie das Wander Nest besuchen.</p>
  <p style="top:919px">Unsere Spezialgebiet sind Reisen in all asiatischen Länder wie Thailand, Vietnam, China und Indien, aber wir sind auf der ganzen Welt zu Hause. Egal ob eine Städtereise in Europa, ein Trip in die USA oder Kanada, oder der Event zum nächsten Heimspiel Ihres Lieblingsvereins.</p>
  <p style="top:951px;text-align:center">Wir machen Ihre Reise zu einem unvergesslichen Erlebnis.</p>
</section>

<footer>
  <div class="abs footer"></div>
  <div class="abs foot-brand">Wander Nest</div>
  <div class="abs foot-text" style="left:194px;top:1049px">Wander-Nest<br>Lindenweg 12<br>86150 Augsburg</div>
  <div class="abs foot-text" style="left:297px;top:1049px">TEL:&nbsp; +49&nbsp; -(0)821 - 555 10 20<br>FAX:&nbsp; +49&nbsp; -(0)821 - 555 10 29<br>info@wandernest-reisen.de</div>
  <div class="abs foot-head">ÖFFNUNGSZEITEN</div>
  <div class="abs foot-text" style="left:435px;top:1049px">MO-FR<br><br>SA<br>MI</div>
  <div class="abs foot-text" style="left:471px;top:1049px">10-13 h<br>14-18 h<br>10-13 h</div>
  <div class="abs foot-text" style="left:452px;top:1081px;letter-spacing:-.3px">Vormittag geschlossen</div>
  <div class="abs foot-rule"></div>
  <div class="abs legal">Copyright 2019&nbsp; |&nbsp;&nbsp; Ihre Firma&nbsp;&nbsp; |&nbsp;&nbsp; Impressum&nbsp;&nbsp; |&nbsp;&nbsp; Datenschutz&nbsp;&nbsp; |&nbsp;&nbsp; Kontakt</div>
</footer>
</body>
</html>
```